Business Card Design for TrailStocked

TrailStocked is an online e-commerce store specializing in Outdoors Gear such as camping equipment, hunting and shooting equipment, tactical gear and more. See complete line at trailstocked.org
Logo: http://www.trailstocked.org/media/ID/Stocked.jpg
http://www.trailstocked.org/media/ID/TrailStocked-blue.jpg

Target Market(s)

20-40 Male

Industry/Entity Type

E-Commerce

```html
<!DOCTYPE html>
<html lang="en">
<head>
<meta charset="utf-8">
<title>TrailStocked Business Card</title>
<link rel="stylesheet" href="https://fonts.googleapis.com/css2?family=Open+Sans:wght@400;600;700&display=swap">
<style>
  :root {
    --navy: #123c66;
    --navy-deep: #0b1a3a;
    --white: #ffffff;
    --ink: #163d68;
    --page: #ece9e4;
  }
  * { margin: 0; padding: 0; box-sizing: border-box; }
  html, body { width: 1200px; height: 900px; overflow: hidden; background: var(--page); }
  body { position: relative; font-family: "Open Sans", sans-serif; }

  .card {
    position: absolute; top: 290px; width: 560px; height: 320px;
    background: var(--white); overflow: hidden;
    box-shadow: 0 4px 14px rgba(0,0,0,0.18);
  }
  .card--front { left: 24px; }
  .card--back { left: 616px; }
  .card__shapes { position: absolute; inset: 0; width: 560px; height: 320px; }

  /* Front */
  .brand { position: absolute; left: 34px; top: 42px; display: flex; align-items: center; gap: 12px; }
  .brand__dot { width: 46px; height: 46px; border-radius: 50%; background: var(--ink); }
  .brand__name { font-weight: 700; font-size: 29px; color: var(--ink); line-height: 1; }
  .tagline-small {
    position: absolute; left: 92px; top: 82px;
    font-size: 12.5px; font-weight: 600; color: var(--ink); letter-spacing: 0.6px;
  }
  .person { position: absolute; left: 30px; top: 200px; width: 220px; text-align: center; color: var(--white); }
  .person__name { font-size: 22px; font-weight: 700; line-height: 1.2; }
  .person__title { font-size: 16px; font-weight: 400; line-height: 1.4; }
  .rule { position: absolute; width: 1px; background: rgba(255,255,255,0.55); }
  .rule--front { left: 266px; top: 178px; height: 122px; }
  .contact { position: absolute; left: 316px; top: 178px; color: var(--white); font-size: 13.5px; line-height: 19px; }
  .contact__address { margin-bottom: 6px; }
  .contact__row { display: flex; align-items: center; gap: 6px; }
  .contact__icon { width: 14px; height: 14px; flex: none; }

  /* Back */
  .back-name {
    position: absolute; left: 22px; top: 150px; width: 110px; text-align: center;
    font-size: 16px; font-weight: 700; color: var(--ink);
  }
  .rule--back { left: 136px; top: 120px; height: 96px; background: var(--ink); width: 2px; }
  .tagline-large {
    position: absolute; left: 162px; top: 134px;
    font-size: 21px; font-weight: 700; color: var(--ink); line-height: 30px;
  }
  .back-url {
    position: absolute; left: 0; right: 0; top: 292px; text-align: center;
    color: var(--white); font-size: 14px; letter-spacing: 3px;
  }
</style>
</head>
<body>

<section class="card card--front">
  <svg class="card__shapes" viewBox="0 0 560 320" aria-hidden="true">
    <path d="M0 148 H330 C362 148 378 140 396 124 L522 0 H560 V320 H0 Z" fill="var(--navy)"/>
    <path d="M370 148 L560 6 V148 Z" fill="var(--navy-deep)"/>
  </svg>
  <div class="brand">
    <span class="brand__dot"></span>
    <span class="brand__name">TrailStocked.com</span>
  </div>
  <p class="tagline-small">Outfitted for the Wild and Beyond</p>

  <div class="person">
    <p class="person__name">Daniel Morrow</p>
    <p class="person__title">Purchasing Manager</p>
  </div>
  <span class="rule rule--front"></span>
  <div class="contact">
    <p class="contact__address">PO BOX 287<br>Fairview, IL 60124</p>
    <p class="contact__row">
      <svg class="contact__icon" viewBox="0 0 14 14"><rect x="4" y="1" width="6" height="12" rx="1" fill="none" stroke="#fff" stroke-width="1.4"/><rect x="5.5" y="3" width="3" height="4" fill="#fff"/></svg>
      555 201 4400</p>
    <p class="contact__row">
      <svg class="contact__icon" viewBox="0 0 14 14"><rect x="3" y="1" width="8" height="12" fill="#fff"/><rect x="5" y="3" width="1.5" height="1.5" fill="var(--navy)"/><rect x="7.5" y="3" width="1.5" height="1.5" fill="var(--navy)"/><rect x="5" y="6" width="1.5" height="1.5" fill="var(--navy)"/><rect x="7.5" y="6" width="1.5" height="1.5" fill="var(--navy)"/><rect x="6" y="10" width="2" height="3" fill="var(--navy)"/></svg>
      555 201 4471</p>
    <p class="contact__row">
      <svg class="contact__icon" viewBox="0 0 14 14"><rect x="1" y="3" width="12" height="8" fill="none" stroke="#fff" stroke-width="1.3"/><path d="M1 3 L7 8 L13 3" fill="none" stroke="#fff" stroke-width="1.3"/></svg>
      Purchasing@TrailStocked.org</p>
    <p class="contact__row">
      <svg class="contact__icon" viewBox="0 0 14 14"><circle cx="7" cy="7" r="5.6" fill="none" stroke="#fff" stroke-width="1.3"/><ellipse cx="7" cy="7" rx="2.4" ry="5.6" fill="none" stroke="#fff" stroke-width="1.1"/><path d="M1.4 7 H12.6" stroke="#fff" stroke-width="1.1"/></svg>
      www.TrailStocked.org</p>
  </div>
</section>

<section class="card card--back">
  <svg class="card__shapes" viewBox="0 0 560 320" aria-hidden="true">
    <rect x="0" y="0" width="560" height="88" fill="var(--navy)"/>
    <path d="M0 246 H300 C332 246 346 240 364 226 L522 88 H560 V320 H0 Z" fill="var(--navy)"/>
    <path d="M356 246 L560 92 V246 Z" fill="var(--navy-deep)"/>
  </svg>
  <p class="back-name">TrailStocked</p>
  <span class="rule rule--back"></span>
  <p class="tagline-large">Outfitted for the Wild<br>and Beyond</p>
  <p class="back-url">www.trailstocked.com</p>
</section>

</body>
</html>
```